Brindle Finance Flyer Design

I would like a high res flyer designed for mass printing. It is for a mortgage and finance broking company in Sydney. We are called Brindle Finance. The wording i would like displayed is the following
Looking For Something Extra from your broker?
Brindle Finance can make all the difference
What we offer you is an extensive range of mortgage and finance products, including:
• Home Loans
• Investment Loans
• Low Doc Loans
• Vehicle Finance
• Equipment Finance
• Commercial Loans
• Refinance
Contact Us
Phone (02) 7412 5830
email info@brindlefinance.com.au
web www.brindlefinance.com.au
Industry/Entity Type
Finance
Look and feel

```html
<!DOCTYPE html>
<html lang="en">
<head>
<meta charset="utf-8">
<title>Brindle Finance Flyer Design_01</title>
<link rel="stylesheet" href="https://fonts.googleapis.com/css2?family=Arimo:wght@400;700&family=Tinos&display=swap">
<style>
  :root {
    --page-bg: #ffffff;
    --sheet-bg: #ffffff;
    --brand-blue: #5ba4dc;
    --band-blue: #5fa6dc;
    --ink: #111111;
    --logo-grey: #555b61;
    --white: #ffffff;
    --photo-light: #e4edf5;
    --photo-mid: #c3d1e0;
    --photo-deep: #8596b3;
  }
  * { margin: 0; padding: 0; box-sizing: border-box; }
  html, body {
    width: 1200px; height: 1000px; overflow: hidden;
    background: var(--page-bg);
    font-family: "Arimo", Arial, sans-serif;
  }
  .canvas { position: relative; width: 1200px; height: 1000px; }

  .flyer {
    position: absolute; left: 303px; top: 59px;
    width: 594px; height: 842px;
    background: var(--sheet-bg);
    box-shadow: 2px 3px 6px rgba(0,0,0,0.35), 0 0 1px rgba(0,0,0,0.25);
    overflow: hidden;
  }

  .brand {
    position: absolute; top: 38px; left: 0; width: 100%;
    display: flex; flex-direction: column; align-items: center;
  }
  .brand-row { display: flex; align-items: center; gap: 8px; }
  .brand-mark { width: 14px; height: 14px; background: var(--logo-grey); }
  .brand-name {
    font-size: 27px; font-weight: 400; color: var(--logo-grey);
    line-height: 1; letter-spacing: -0.2px;
  }
  .brand-tagline {
    margin-top: 3px; font-size: 9.5px; color: var(--logo-grey);
    letter-spacing: 0.1px;
  }

  .headline {
    position: absolute; top: 114px; left: 0; width: 100%;
    text-align: center; color: var(--brand-blue);
    font-size: 20.5px; font-weight: 700; line-height: 25px;
  }

  .hero-photo {
    position: absolute; top: 200px; left: 0; width: 100%; height: 342px;
    background: linear-gradient(100deg, var(--photo-light) 0%, #f2f6fa 40%, var(--photo-mid) 70%, var(--photo-deep) 100%);
  }

  .offer-band {
    position: absolute; top: 541px; left: 0; width: 100%; height: 160px;
    background: var(--band-blue); text-align: center;
  }
  .offer-intro {
    margin-top: 27px; color: var(--ink);
    font-size: 19.8px; font-weight: 700; line-height: 25px;
  }
  .product-list {
    list-style: none; margin-top: 16px;
    color: var(--white); font-size: 15px; line-height: 20px;
  }
  .product-list li { display: inline; }
  .product-list li::before {
    content: "\25CF"; color: var(--ink); margin: 0 7px 0 8px;
    font-size: 10px; vertical-align: 2px;
  }

  .contact {
    position: absolute; top: 729px; left: 40px;
  }
  .contact-title {
    color: var(--brand-blue); font-size: 20px; font-weight: 700;
    margin-bottom: 5px;
  }
  .contact-line { font-size: 15px; color: var(--ink); line-height: 21px; }

  .web-address {
    position: absolute; top: 776px; right: 40px;
    color: var(--brand-blue); font-size: 19.5px; font-weight: 700;
  }

  .caption {
    position: absolute; top: 921px; left: 0; width: 100%;
    text-align: center; font-family: "Tinos", "Times New Roman", serif;
    font-size: 20px; color: var(--ink);
  }
</style>
</head>
<body>
<div class="canvas">
  <article class="flyer">
    <header class="brand">
      <div class="brand-row">
        <span class="brand-mark"></span>
        <span class="brand-name">Brindle Finance</span>
      </div>
      <div class="brand-tagline">mortgage and finance broking services</div>
    </header>

    <h1 class="headline">Looking For Something Extra from your broker?<br>Brindle Finance can make all the difference</h1>

    <div class="hero-photo" role="img" aria-label="Photo: bright office corridor with business people walking, motion blurred"></div>

    <section class="offer-band">
      <p class="offer-intro">What we offer you is an extensive range of<br>mortgage and finance products, including:</p>
      <ul class="product-list">
        <li>Home Loans</li>
        <li>Investment Loans</li>
        <li>Low Doc Loans</li>
        <li>Vehicle Finance</li><br>
        <li>Equipment Finance</li>
        <li>Commercial Loans</li>
        <li>Refinance</li>
      </ul>
    </section>

    <section class="contact">
      <h2 class="contact-title">Contact Us</h2>
      <p class="contact-line">Phone: (02) 7412 5830</p>
      <p class="contact-line">Email: info@brindlefinance.com.au</p>
    </section>
    <p class="web-address">www.brindlefinance.com.au</p>
  </article>

  <p class="caption">Brindle Finance Flyer Design_01</p>
</div>
</body>
</html>
```